Great Opportunity !! Masters in Business Analytics College Course

the size is Full Page, with bleed*
8”x 10.75" plus 0.25" bleed.
please leave one inch for footer
the purpose is attract students to join this college program .
this is for students in USA .
college age of around 24 years old
I am looking for a flyer that is unique and shows creativity .
A flyer that people would want to look at it because it is unique.
you can choose either vector, text ,or picture.
if you do picture it should be a white USA citizen wearing a white solid shirt and not long hair

Target Market(s)

USA students about 23 in age to join this college program

Industry/Entity Type

education

Colors
0054AA
0677BA
7BADD7
CADEEF
E8F1F8
0094D4
00A9DD
6FCCEA
C7EBF8
E9F6FB

Requirements
Must have
• the text should not be crowded .. .. .. the ad should not be full of text
Should not have
• not have very large text .. it should not be a flyer that is full of text .. you have to figure out how to avoid looking at the ad and it is very busy with text

```html
<!DOCTYPE html>
<html lang="en">
<head>
<meta charset="UTF-8">
<title>Master's in Business Analytics – Flyer</title>
<link href="https://fonts.googleapis.com/css2?family=Montserrat:wght@500;600;700;800&display=swap" rel="stylesheet">
<style>
  :root{
    --page-bg:#cfcfcf;
    --paper:#ffffff;
    --ink:#111111;
    --muted:#8a8a8a;
    --orange:#f5862b;
    --pink:#ec1a8c;
    --deep-blue:#1b5fa6;
    --sky:#2d9cdb;
    --cyan:#15a8d2;
    --heading-blue:#1a5c9e;
    --yellow:#f2c200;
  }
  *{margin:0;padding:0;box-sizing:border-box}
  html,body{width:1200px;height:1200px;overflow:hidden}
  body{background:var(--page-bg);font-family:'Montserrat',sans-serif;position:relative}
  .flyer{position:absolute;left:183px;top:40px;width:833px;height:1120px;background:var(--paper);overflow:hidden}
  .hero{position:absolute;left:0;top:0;width:833px;height:521px}
  .hero svg{display:block}
  .headline{position:absolute;left:41px;top:138px;color:#fff;font-weight:800;font-size:44px;line-height:54px;letter-spacing:-0.3px}
  .program{position:absolute;left:39px;top:424px;color:#fff;font-weight:700;font-size:24px;line-height:35px}
  .pitch{position:absolute;left:41px;top:538px;width:500px;color:var(--ink);font-weight:800;font-size:29px;line-height:42px}
  .salary{position:absolute;left:41px;top:620px;display:flex;align-items:center;gap:18px}
  .salary-figure{color:var(--orange);font-weight:800;font-size:54px;letter-spacing:-1px;line-height:1}
  .salary-source{font-size:13px;font-weight:500;color:var(--ink)}
  .divider{position:absolute;left:563px;top:547px;width:2px;height:131px;background:var(--orange)}
  .roles{position:absolute;left:587px;top:562px;list-style:none}
  .roles li{display:flex;align-items:center;gap:6px;font-size:14.5px;font-weight:700;height:26.5px}
  .hired{position:absolute;left:41px;top:696px;width:751px;height:100px;border-radius:22px;overflow:hidden;display:flex}
  .hired-label{width:250px;background:linear-gradient(90deg,var(--pink),var(--orange));color:#fff;font-weight:700;font-size:25px;line-height:37px;padding:16px 0 0 23px}
  .hired-list{flex:1;background:var(--sky);border-radius:22px 0 0 22px;margin-left:-16px;display:grid;grid-template-columns:170px 130px 1fr;grid-auto-rows:39px;padding:10px 0 0 22px;align-content:start}
  .hired-list span{display:flex;align-items:center;gap:10px;color:#fff;font-weight:700;font-size:25px}
  .accreditation{position:absolute;left:41px;top:818px;color:var(--heading-blue);font-weight:800;font-size:24.5px;line-height:35px}
  .open-house{position:absolute;left:447px;top:817px;width:345px;height:107px;background:var(--orange);border-radius:22px;color:#fff;padding:12px 0 0 25px}
  .open-house h2{font-size:25px;font-weight:800;line-height:32px}
  .open-house .date{font-size:18.5px;font-weight:700;line-height:28px}
  .open-house .contact{display:flex;align-items:center;gap:8px;font-size:14px;font-weight:500;line-height:22px}
  .open-house .contact b{font-weight:700}
  .facts{position:absolute;left:0;top:950px;width:833px;height:50px}
  .fact{position:absolute;display:flex;align-items:center;gap:11px;color:var(--muted);font-weight:600;font-size:17px;line-height:24.5px}
  .location{position:absolute;left:41px;top:1048px;font-size:14.5px;font-weight:500;color:var(--ink)}
</style>
</head>
<body>
<main class="flyer">
  <div class="hero">
    <svg width="833" height="521" viewBox="0 0 833 521" aria-hidden="false">
      <defs>
        <linearGradient id="heroTone" x1="0" y1="0" x2="1" y2="0.3">
          <stop offset="0" stop-color="#1b5aa3"/>
          <stop offset="0.55" stop-color="#1887c4"/>
          <stop offset="1" stop-color="#12b3d8"/>
        </linearGradient>
        <linearGradient id="waveTone" x1="0" y1="0" x2="1" y2="0">
          <stop offset="0" stop-color="#ec1a8c"/>
          <stop offset="0.55" stop-color="#f2545a"/>
          <stop offset="1" stop-color="#f5862b"/>
        </linearGradient>
      </defs>
      <path role="img" aria-label="Photo of a smiling student in a white sweater holding books in front of a campus building"
            d="M0,125 C200,95 340,62 470,70 C600,80 700,130 833,172 L833,521 L0,521 Z" fill="url(#heroTone)"/>
      <path class="hero-wave" d="M0,78 C180,110 320,45 470,48 C610,51 720,120 800,160 C815,166 825,168 833,166 L833,174 C700,140 600,82 470,70 C340,62 200,95 0,125 Z" fill="url(#waveTone)"/>
    </svg>
    <h1 class="headline">Do you have an<br>ANALYTICAL mind<br>and seeking a<br>PROFITABLE<br>career?</h1>
    <p class="program">A Master's in Business Analytics-<br>Northvale State University **</p>
  </div>

  <p class="pitch">can prepare you for in-demand jobs with a median salary of</p>
  <div class="salary">
    <span class="salary-figure">$100k+</span>
    <span class="salary-source">(National Labor Data 2023)</span>
  </div>

  <div class="divider"></div>
  <ul class="roles">
    <li><svg width="15" height="15" viewBox="0 0 20 20"><circle cx="10" cy="10" r="10" fill="#f5862b"/><path d="M5.5 10.3l3 3 6-6" fill="none" stroke="#fff" stroke-width="2.6" stroke-linecap="round" stroke-linejoin="round"/></svg>BI Developer</li>
    <li><svg width="15" height="15" viewBox="0 0 20 20"><circle cx="10" cy="10" r="10" fill="#f5862b"/><path d="M5.5 10.3l3 3 6-6" fill="none" stroke="#fff" stroke-width="2.6" stroke-linecap="round" stroke-linejoin="round"/></svg>Data Analyst</li>
    <li><svg width="15" height="15" viewBox="0 0 20 20"><circle cx="10" cy="10" r="10" fill="#f5862b"/><path d="M5.5 10.3l3 3 6-6" fill="none" stroke="#fff" stroke-width="2.6" stroke-linecap="round" stroke-linejoin="round"/></svg>Data Scientist</li>
    <li><svg width="15" height="15" viewBox="0 0 20 20"><circle cx="10" cy="10" r="10" fill="#f5862b"/><path d="M5.5 10.3l3 3 6-6" fill="none" stroke="#fff" stroke-width="2.6" stroke-linecap="round" stroke-linejoin="round"/></svg>Data Developer</li>
  </ul>

  <section class="hired">
    <div class="hired-label">Graduates<br>were hired at:</div>
    <div class="hired-list">
      <span><svg width="24" height="24" viewBox="0 0 20 20"><circle cx="10" cy="10" r="10" fill="#f2c200"/><path d="M5.5 10.3l3 3 6-6" fill="none" stroke="#fff" stroke-width="2.4" stroke-linecap="round" stroke-linejoin="round"/></svg>Kestrel</span>
      <span><svg width="24" height="24" viewBox="0 0 20 20"><circle cx="10" cy="10" r="10" fill="#f2c200"/><path d="M5.5 10.3l3 3 6-6" fill="none" stroke="#fff" stroke-width="2.4" stroke-linecap="round" stroke-linejoin="round"/></svg>Orbix</span>
      <span><svg width="24" height="24" viewBox="0 0 20 20"><circle cx="10" cy="10" r="10" fill="#f2c200"/><path d="M5.5 10.3l3 3 6-6" fill="none" stroke="#fff" stroke-width="2.4" stroke-linecap="round" stroke-linejoin="round"/></svg>Harborline</span>
      <span><svg width="24" height="24" viewBox="0 0 20 20"><circle cx="10" cy="10" r="10" fill="#f2c200"/><path d="M5.5 10.3l3 3 6-6" fill="none" stroke="#fff" stroke-width="2.4" stroke-linecap="round" stroke-linejoin="round"/></svg>Vantor</span>
      <span><svg width="24" height="24" viewBox="0 0 20 20"><circle cx="10" cy="10" r="10" fill="#f2c200"/><path d="M5.5 10.3l3 3 6-6" fill="none" stroke="#fff" stroke-width="2.4" stroke-linecap="round" stroke-linejoin="round"/></svg>Voltra</span>
    </div>
  </section>

  <p class="accreditation">*** GBAC Accreditation.<br>A distinction held by only 5%<br>of business schools globally.</p>

  <section class="open-house">
    <h2>OPEN HOUSE</h2>
    <p class="date">Wednesday, April 20, 7:30 pm.</p>
    <p class="contact"><svg width="19" height="14" viewBox="0 0 19 14"><rect x="0.5" y="0.5" width="18" height="13" rx="1.5" fill="#fff"/><path d="M1.5 1.8l8 6 8-6" fill="none" stroke="#f5862b" stroke-width="1.6"/></svg><span><b>info@northvale.edu</b> for the link!</span></p>
  </section>

  <div class="facts">
    <div class="fact" style="left:66px;top:0">
      <svg width="36" height="36" viewBox="0 0 20 20"><circle cx="10" cy="10" r="10" fill="#f5862b"/><path d="M5.5 10.3l3 3 6-6" fill="none" stroke="#fff" stroke-width="2.3" stroke-linecap="round" stroke-linejoin="round"/></svg>
      <span>Men &amp; Women<br>Program</span>
    </div>
    <div class="fact" style="left:289px;top:0;height:49px">
      <svg width="36" height="36" viewBox="0 0 20 20"><circle cx="10" cy="10" r="10" fill="#f5862b"/><path d="M5.5 10.3l3 3 6-6" fill="none" stroke="#fff" stroke-width="2.3" stroke-linecap="round" stroke-linejoin="round"/></svg>
      <span>21 months</span>
    </div>
    <div class="fact" style="left:473px;top:0">
      <svg width="36" height="36" viewBox="0 0 20 20"><circle cx="10" cy="10" r="10" fill="#f5862b"/><path d="M5.5 10.3l3 3 6-6" fill="none" stroke="#fff" stroke-width="2.3" stroke-linecap="round" stroke-linejoin="round"/></svg>
      <span>Hybrid with one weekly<br>in-person evening meeting</span>
    </div>
  </div>

  <p class="location">Cedar Ridge, NJ, USA</p>
</main>
</body>
</html>
```